Letterhead creation for military law attorney

I need letterhead design for my business. We are now only doing military law and need to change address, logo and vision. I like the idea of using an eagle or a jolly roger flag

Target Market(s)

Military Law Clients

Colors
3176b5
85abd2

Requirements
Must have
• We are defending people against the government
Nice to have
• Jolly Roger Flag

```html
<!DOCTYPE html>
<html lang="en">
<head>
<meta charset="utf-8">
<title>Hartwell Law Letterhead</title>
<link href="https://fonts.googleapis.com/css2?family=Open+Sans:wght@400;600&display=swap" rel="stylesheet">
<style>
  :root {
    --backdrop: #2e2e2e;
    --paper: #ffffff;
    --ink: #111111;
    --body-text: #5a5a5a;
    --signature-tone: #ececec;
  }
  * { margin: 0; padding: 0; box-sizing: border-box; }
  html, body {
    width: 1200px; height: 900px; overflow: hidden;
    background: var(--backdrop);
    font-family: "Open Sans", Arial, sans-serif;
  }
  .letterhead {
    position: absolute; left: 300px; top: 26px;
    width: 600px; height: 848px;
    background: var(--paper);
    overflow: hidden;
  }
  .brand {
    position: absolute; left: 44px; top: 54px;
    display: flex; align-items: center; gap: 10px;
  }
  .brand-dot {
    width: 22px; height: 22px; border-radius: 50%;
    background: var(--ink);
  }
  .brand-name {
    font-size: 13px; font-weight: 400; letter-spacing: 3px;
    color: var(--ink); text-transform: uppercase;
  }
  .header-rule {
    position: absolute; left: 44px; right: 40px; top: 88px;
    border-top: 1.5px solid var(--ink);
  }
  .contact {
    position: absolute; right: 40px; top: 46px;
    font-size: 7.5px; line-height: 1.45; color: var(--ink);
    font-style: normal;
  }
  .letter-date {
    position: absolute; left: 110px; top: 190px;
    font-size: 10px; color: var(--body-text);
  }
  .letter-body {
    position: absolute; left: 110px; top: 236px; width: 430px;
    font-size: 9.5px; line-height: 22px; color: var(--body-text);
  }
  .letter-body p + p { margin-top: 12px; }
  .sign-off {
    position: absolute; right: 40px; top: 528px; width: 112px;
  }
  .signature {
    width: 96px; height: 30px; border-radius: 4px;
    background: var(--signature-tone);
  }
  .signer-name, .signer-role {
    font-size: 8.5px; line-height: 1.4; color: var(--body-text);
    margin-left: 30px;
  }
  .signer-name { margin-top: 4px; }
  .swoosh {
    position: absolute; left: 0; bottom: 0;
    width: 600px; height: 848px; display: block;
  }
</style>
</head>
<body>
  <main class="letterhead">
    <header>
      <div class="brand">
        <span class="brand-dot"></span>
        <span class="brand-name">Hartwell Law, PLLC</span>
      </div>
      <address class="contact">
        P: (555) 014-2270<br>
        F: (555) 014-2271<br>
        PO Box 318 Fairmont, TN 37000
      </address>
      <div class="header-rule"></div>
    </header>

    <p class="letter-date">Date, 10 September, 2020</p>

    <section class="letter-body">
      <p>This is a sample letter that has been placed to demonstrate typing remat (Your Company). letterhead design. When positioned properly, it will serve to work in harmony with all other elements letterhead. This letterhead design is meant to project an image. This letterhead design is meant project an image of professionalism reliability. By using simple aligen we have created a very spacious feeling. The simplicity suggest rengththe spaciousnes contributes h aesthetics the layout. These basic qualities along with the (Your Company) look and helps reinforce the (Your Company) brand. letterhead design is meant to project an image p design. When positioned properly, it will serve to work in harmony all the other elements letterhead. sionalism and reliability.</p>
      <p>This letterhead design is based on the (Form of your logo) form (Your Company) logo. Each stationery we have created a very spacious feeling. The simplicity suggests strength the spaciousnes contribute part of the (Form of your logo).</p>
    </section>

    <div class="sign-off">
      <div class="signature" role="img" aria-label="Handwritten signature of Daniel Crane"></div>
      <p class="signer-name">Daniel Crane</p>
      <p class="signer-role">Manager</p>
    </div>

    <svg class="swoosh" viewBox="0 0 600 848" aria-hidden="true">
      <path d="M0 848 L0 832 C250 828 380 790 440 722 C490 666 530 650 600 644 L600 848 Z" fill="var(--ink)"/>
      <path d="M0 842 C260 836 400 800 462 734 C502 690 532 668 578 652" fill="none" stroke="var(--paper)" stroke-width="3"/>
    </svg>
  </main>
</body>
</html>
```